LinkedIn Cover Image

We need a Linked In Cover Image for our Linked In Business Page.

The dimensions needed are: 1536 x 768px.

Here's a link to our website: www.bramwellrenewal.com
LinkedIn Profile: https://www.profilehub.example/company/bramwell-renewal-services/

Font styles to use
Sans Serif

Colors

Designer to choose colors to be used in the design.

```html
<!DOCTYPE html>
<html lang="en">
<head>
<meta charset="utf-8">
<title>Bramwell Renewal Services – Cover Image</title>
<link href="https://fonts.googleapis.com/css2?family=Open+Sans:wght@400;600;700&family=Roboto+Condensed:wght@400;500&display=swap" rel="stylesheet">
<style>
  :root {
    --page-bg: #d9d9d9;
    --paper: #ffffff;
    --orange: #f08a24;
    --orange-light: #f6ad67;
    --teal: #3f6b7a;
    --label: #454545;
    --divider: #c8c8c8;
    --star-fill: #e6e6e6;
    --mascot-a: #3556a8;
    --mascot-b: #f2c230;
  }
  * { margin: 0; padding: 0; box-sizing: border-box; }
  html, body { width: 1200px; height: 900px; overflow: hidden; background: var(--page-bg); }
  .cover {
    position: absolute; left: 81px; top: 171px;
    width: 1043px; height: 520px;
    background: var(--paper);
    font-family: "Open Sans", sans-serif;
  }
  .cover svg.frame { position: absolute; inset: 0; }
  .mascot {
    position: absolute; left: 2px; top: 42px; width: 136px; height: 134px;
    border-radius: 50%;
    background: radial-gradient(circle at 45% 45%, var(--mascot-a) 0 45%, #d6deef 60%, rgba(214,222,239,0) 71%);
  }
  .brand-name {
    position: absolute; left: 168px; top: 66px; width: 400px;
    color: var(--orange); font-weight: 700; font-size: 34px; line-height: 40px;
    text-transform: uppercase; letter-spacing: 0.5px;
  }
  .emergency {
    position: absolute; left: 648px; top: 26px; color: #fff; line-height: 1;
  }
  .emergency .label { font-size: 37px; font-weight: 400; }
  .emergency .number { font-size: 56px; font-weight: 400; margin-top: 10px; letter-spacing: 0.3px; }
  .website {
    position: absolute; right: 16px; top: 172px; color: #fff;
    font-size: 28px; font-weight: 700; letter-spacing: 0.2px;
  }
  .services { position: absolute; left: 0; top: 0; width: 100%; height: 100%; }
  .service {
    position: absolute; top: 240px; width: 200px; text-align: center;
    font-family: "Roboto Condensed", sans-serif; font-weight: 500;
    font-size: 18px; line-height: 27px; color: var(--label); text-transform: uppercase;
  }
  .service svg { display: block; margin: 0 auto 12px; }
  .service-water { left: 119px; }
  .service-fire { left: 321px; }
  .service-mold { left: 522px; }
  .service-special { left: 723px; }
</style>
</head>
<body>
<main class="cover">
  <svg class="frame" width="1043" height="520" viewBox="0 0 1043 520">
    <rect x="0" y="0" width="620" height="11" fill="var(--orange)"/>
    <polygon points="620,0 1043,0 1043,151 590,151" fill="var(--teal)"/>
    <polygon points="588,159 1043,159 1043,215 580,215" fill="var(--orange)"/>
    <rect x="0" y="205" width="578" height="10" fill="var(--orange)"/>
    <line x1="322" y1="255" x2="322" y2="390" stroke="var(--divider)" stroke-width="2"/>
    <line x1="519" y1="255" x2="519" y2="390" stroke="var(--divider)" stroke-width="2"/>
    <line x1="723" y1="255" x2="723" y2="390" stroke="var(--divider)" stroke-width="2"/>
    <line x1="28" y1="486" x2="421" y2="486" stroke="var(--teal)" stroke-width="3"/>
    <line x1="623" y1="486" x2="1015" y2="486" stroke="var(--teal)" stroke-width="3"/>
    <g class="social-dots" fill="var(--teal)">
      <circle cx="456" cy="485" r="18"/>
      <circle cx="499" cy="485" r="18"/>
      <circle cx="542" cy="485" r="18"/>
      <circle cx="587" cy="485" r="18"/>
    </g>
  </svg>

  <div class="mascot" role="img" aria-label="Cartoon knight mascot holding a cleaning wand over a water puddle"></div>
  <div class="brand-name">Bramwell Renewal<br>Services</div>

  <div class="emergency">
    <div class="label">Emergency Line:</div>
    <div class="number">877-555-0142</div>
  </div>
  <div class="website">www.bramwellrenewal.com</div>

  <section class="services">
    <div class="service service-water">
      <svg width="140" height="140" viewBox="0 0 140 140">
        <circle cx="70" cy="70" r="65" fill="#fff" stroke="var(--orange)" stroke-width="7"/>
        <path d="M70 26 C78 50 94 66 94 86 A24 24 0 0 1 46 86 C46 66 62 50 70 26Z" fill="var(--orange)"/>
        <path d="M70 70 C74 80 80 86 80 93 A10 10 0 0 1 60 93 C60 86 66 80 70 70Z" fill="var(--orange-light)"/>
      </svg>
      Water and Flood<br>Restoration
    </div>
    <div class="service service-fire">
      <svg width="140" height="140" viewBox="0 0 140 140">
        <circle cx="70" cy="70" r="65" fill="#fff" stroke="var(--orange)" stroke-width="7"/>
        <path d="M72 24 C84 42 96 56 96 82 A26 26 0 0 1 44 82 C44 66 52 58 58 50 C60 60 62 64 66 66 C64 50 66 36 72 24Z" fill="var(--orange)"/>
        <path d="M70 76 C76 84 82 90 82 98 A12 12 0 0 1 58 98 C58 90 64 84 70 76Z" fill="var(--orange-light)"/>
      </svg>
      Fire and Smoke<br>Restoration
    </div>
    <div class="service service-mold">
      <svg width="140" height="140" viewBox="0 0 140 140">
        <circle cx="70" cy="70" r="65" fill="#fff" stroke="var(--orange)" stroke-width="7"/>
        <path d="M46 50 C46 30 94 30 94 50 L94 62 L46 62Z" fill="var(--orange)"/>
        <path d="M50 62 L90 62 L86 98 L54 98Z" fill="none" stroke="var(--orange)" stroke-width="4"/>
        <circle cx="48" cy="94" r="14" fill="var(--orange)"/>
        <circle cx="92" cy="94" r="14" fill="var(--orange)"/>
        <rect x="60" y="86" width="20" height="20" rx="4" fill="var(--orange)"/>
      </svg>
      Mold<br>Remediation
    </div>
    <div class="service service-special">
      <svg width="140" height="140" viewBox="0 0 140 140">
        <circle cx="70" cy="70" r="65" fill="var(--star-fill)" stroke="var(--orange)" stroke-width="7"/>
        <polygon points="70,22 81,56 117,56 88,77 99,112 70,91 41,112 52,77 23,56 59,56" fill="#fff" stroke="var(--orange)" stroke-width="1.5"/>
      </svg>
      Specialty<br>Services
    </div>
  </section>
</main>
</body>
</html>
```